Gewinnspielseite
Zielgruppe
Familen mit Kindern
Aufgabenstellung
Design für eine Gewinnspiel bei dem freier Eintritt für 1 Jahr in alle Freizeitparks in Deutschland verlost werden soll. Ablauf wäre das die Gewinnerfamilie uns den Eintrittsbeleg zusendet und wir diesen dann erstatten bis zu einer maximalen Höhe von 5.000 Euro.
Menüpunkte: Startseite, Teilnahmebedingungen, Preisdetails, Teilnehmen, Datenschutz.
Es soll eine Intro-Seite auf der der Preis groß heraus gestellt ist gestaltet werden mit den
entsprechenden Menüpunkten sowie eine Template-Seite in der wir dann alle notwendigen Inhalte einfügen können.
Gewinnspiel von uns finden Sie auf www.lostrommel-beispiel.de damit Sie sich ein Bild über die bisherigen Gewinnspiele machen können.
WICHTIG: Es soll nur die Eingangsseite und eine Template Seite erstellt werden. Die komplette Programmierung bzw. Füllung mit Inhalten wird von uns gemacht!

```html
<!DOCTYPE html>
<html lang="de">
<head>
<meta charset="utf-8">
<title>Parkglück – Freier Eintritt</title>
<link rel="stylesheet" href="https://fonts.googleapis.com/css2?family=Dosis:wght@400;500;600;700&family=Yanone+Kaffeesatz:wght@400;600&family=Roboto:wght@700&display=swap">
<style>
  :root{
    --sky-top:#e3f4fa;
    --sky-bottom:#3d9cbf;
    --footer:#0e4a62;
    --nav-top:#3cc0e4;
    --nav-bottom:#1a92c4;
    --content:#bfe8f6;
    --teal:#3fa8c2;
    --teal-dark:#2b8aa6;
    --ink:#1d4a6b;
    --body:#2c4d62;
    --white:#ffffff;
    --brand:#2a7fb4;
  }
  *{margin:0;padding:0;box-sizing:border-box}
  html,body{width:961px;height:1200px;overflow:hidden}
  body{
    position:relative;
    background:linear-gradient(180deg,var(--sky-top) 0%,#9fd6ea 45%,var(--sky-bottom) 100%);
    font-family:"Dosis",sans-serif;
  }
  .page{position:absolute;left:119px;top:86px;width:720px;height:986px;background:var(--content);overflow:hidden}
  .page::before{
    content:"";position:absolute;left:-200px;top:420px;width:1200px;height:900px;border-radius:50%;
    background:radial-gradient(ellipse at center,rgba(255,255,255,.25),rgba(255,255,255,0) 60%);
  }
  .main-nav{
    position:absolute;left:0;top:0;width:720px;height:70px;
    background:linear-gradient(180deg,var(--nav-top),var(--nav-bottom) 80%,#7fd3ee 100%);
    display:flex;justify-content:space-between;align-items:center;padding:0 20px 12px;
  }
  .main-nav a{font-family:"Roboto",sans-serif;font-weight:700;font-size:12px;color:var(--white);text-decoration:none;letter-spacing:.3px}
  .brand-strip{position:absolute;left:0;top:70px;width:720px;height:13px;background:#e9f7fc}
  .brand-name{
    position:absolute;right:40px;top:62px;z-index:5;
    font-family:"Dosis",sans-serif;font-weight:700;font-size:28px;line-height:30px;
    color:var(--brand);letter-spacing:1px;
  }
  .hero{position:absolute;left:0;top:83px;width:720px;height:193px}
  .hero-photo{
    position:absolute;inset:0;
    background:linear-gradient(90deg,#2f8fbf 0%,#5cb6dc 40%,#4aa9d4 70%,#2d8ec0 100%);
  }
  .hero-animal{position:absolute;left:48px;top:0;width:104px;height:193px;background:linear-gradient(180deg,#6b6358,#3b3833)}
  .hero-coaster{position:absolute;left:470px;top:38px;width:250px;height:130px;border-radius:60% 40% 0 0;background:linear-gradient(135deg,#e0a12e,#c8532a 60%,#7a3a25)}
  .hero-text{position:absolute;left:154px;top:50px;color:var(--white);font-family:"Yanone Kaffeesatz",sans-serif}
  .hero-text .kicker{font-size:20px;color:#1d3d55;font-weight:600}
  .hero-text .title{font-size:58px;font-weight:600;letter-spacing:3px;line-height:.95}
  .hero-text .sub{font-size:17px;color:#1d3d55;font-weight:600}
  .prize-box{
    position:absolute;left:97px;top:320px;width:425px;height:97px;
    background:linear-gradient(180deg,var(--teal),var(--teal-dark));
    border:2px solid #8fd9ec;color:var(--white);
    font-family:"Yanone Kaffeesatz",sans-serif;font-size:29px;line-height:34px;padding:13px 14px;
  }
  .prize-note{position:absolute;left:474px;top:360px;width:138px;height:130px;background:#f7f7f3;transform:rotate(-8deg);box-shadow:2px 4px 6px rgba(0,0,0,.25);z-index:2}
  .page-title{position:absolute;left:22px;top:468px;font-size:30px;font-weight:500;color:var(--ink)}
  .page-body{position:absolute;left:22px;top:544px;width:690px;font-size:15.2px;line-height:19.5px;color:var(--body)}
  .page-body p{margin-bottom:15px}
  .cta{
    position:absolute;left:423px;top:914px;width:231px;height:47px;
    background:linear-gradient(180deg,var(--teal),var(--teal-dark));border:2px solid #8fd9ec;
    color:var(--white);font-family:"Dosis",sans-serif;font-weight:600;font-size:27px;letter-spacing:3px;
    display:flex;align-items:center;justify-content:center;text-decoration:none;
  }
  .site-footer{position:absolute;left:0;bottom:0;width:961px;height:36px;background:var(--footer);display:flex;align-items:center;justify-content:center}
  .site-footer a{font-size:13px;color:var(--white);text-decoration:none}
</style>
</head>
<body>
  <main class="page">
    <nav class="main-nav">
      <a href="#">STARTSEITE</a>
      <a href="#">TEILNAHMEBEDINGUNGEN</a>
      <a href="#">PREISDETAILS</a>
      <a href="#">TEILNEHMEN</a>
      <a href="#">DATENSCHUTZ</a>
    </nav>
    <div class="brand-strip"></div>
    <section class="hero">
      <div class="hero-photo" role="img" aria-label="Freizeitpark mit Achterbahn vor blauem Himmel"></div>
      <div class="hero-animal" role="img" aria-label="Affe an einem Kletterseil"></div>
      <div class="hero-coaster" role="img" aria-label="Gelb-rote Achterbahn mit Wagen"></div>
      <div class="hero-text">
        <div class="kicker">1 Jahr lang</div>
        <div class="title">FREIER EINTRITT</div>
        <div class="sub">freier Eintritt in alle deutschen Freizeitparks</div>
      </div>
    </section>
    <div class="brand-name">PARKGLÜCK</div>
    <div class="prize-box">Gewinnen Sie ein Jahr kostenlosen Eintritt<br>in alle Freizeitparks Deutschlands !</div>
    <div class="prize-note" role="img" aria-label="Angepinnter Notizzettel: Im Gesamtwert von bis zu 5.000 €"></div>
    <h1 class="page-title">Lorem ipsum dolor sit amet elitr et</h1>
    <div class="page-body">
      <p>Lorem ipsum dolor sit amet, consetetur sadipscing elitr, sed diam nonumy eirmod tempor invidunt ut labore et dolore<br>magna aliquyam erat, sed diam voluptua. At vero eos et accusam et justo duo dolores et ea rebum.<br>Stet clita kasd gubergren, no sea takimata sanctus est Lorem ipsum dolor sit amet. Lorem ipsum dolor sit amet,<br>consetetur sadipscing elitr, sed diam nonumy eirmod tempor invidunt ut labore et dolore magna aliquyam erat,<br>sed diam voluptua. At vero eos et accusam et justo duo dolores et ea rebum. Stet clita kasd gubergren,<br>no sea takimata sanctus est Lorem ipsum dolor sit amet. Lorem ipsum dolor sit amet, consetetur sadipscing elitr,<br>sed diam nonumy eirmod tempor invidunt ut labore et dolore magna aliquyam erat, sed diam voluptua.<br>At vero eos et accusam et justo duo dolores et ea rebum. Stet clita kasd gubergren,<br>no sea takimata sanctus est Lorem ipsum dolor sit amet.</p>
      <p>Duis autem vel eum iriure dolor in hendrerit in vulputate velit esse molestie consequat, vel illum dolore eu feugiat<br>nulla facilisis at vero eros et accumsan et iusto odio dignissim qui blandit praesent luptatum zzril delenit augue duis<br>dolore te feugait nulla facilisi. Lorem ipsum dolor sit amet, consectetuer adipiscing elit, sed diam nonummy nibh<br>euismod tincidunt ut laoreet dolore magna aliquam erat volutpat.</p>
      <p>Ut wisi enim ad minim veniam, quis nostrud exerci tation ullamcorper suscipit lobortis nisl ut aliquip ex ea commodo<br>consequat. Duis autem vel eum iriure dolor in hendrerit in vulputate velit esse molestie consequat,<br>vel illum dolore eu feugiat nulla facilisis at vero eros et accumsan et iusto odio dignissim qui blandit praesent<br>luptatum zzril delenit augue duis dolore te feugait nulla facilisi.</p>
    </div>
    <a class="cta" href="#">100% gratis</a>
  </main>
  <footer class="site-footer"><a href="#">Impressum</a></footer>
</body>
</html>
```